Restaurant Menu New Design

Hello Designers,

Amber Fern is a casual family oriented dine-in restaurant, we serve American Italian dishes like Pizza, Pasta, and Sandwiches.

We are excited about adding some new delicious dishes and recipes to our menu. And we are looking for a talented and creative designer to design it.

The menu is a 12 page black leather book, page size is:
6.5" X 11.69" (16.51 cm X 29.69 cm)

Below is the scope of work and requirements:

1) Design a completely all new, creative, and beautiful menu, including cover page, amber fern oven intro. page, interior pages, and kids menu page.

2) Design a take out edition of the menu. It will be exactly the same as the dine-in menu, but with the addition of a back cover page with info such as contacts, social media, location map, etc…

3) Files are required in Adobe Illustrator format. Layers should be organized, all text should be editable, and all the food pictures easy to change.

4) This is a two language menu, so you are required to make space in the design for a second language. The easiest way to do that is have every item listed in English twice, then I will edit the second text with Illustrator.

5) In your initial design submission, the minimum you are required to submit are these 4 pages:
– Cover page
– Typical interior menu page
– Kids menu page
– Take-out menu back cover page

If your initial design is selected, then you are required to submit all remaining pages to complete the project.

In the link below, you will find:
1) Logo
2) New menu text in Excel
3) Food images (will take some time to upload)
4) The old dine-in and take out menu designs

https://files.quorvexa-share.com/sh/k7wmtzb4fqa9nxe/BBBrTpvLd83JfhRqZe5Y2P7m?dl=0

Thank you for stopping by and reading this brief. I hope you like this project and enjoy designing our new menu. Please let me know if you have any questions.

Cheers!

Project Deadline Extended
Reason: We have decided to extend the deadline due to the low number of submissions which was much lower than the expected submissions we were give by Vintrel Hub.

```html
<!DOCTYPE html>
<html lang="en">
<head>
<meta charset="utf-8">
<title>Amber Fern — Pasta</title>
<link rel="stylesheet" href="https://fonts.googleapis.com/css2?family=Fira+Sans+Extra+Condensed:ital,wght@0,300;0,400;0,600;1,300;1,400;1,600;1,800&family=Josefin+Sans:wght@100;200&display=swap">
<style>
  :root {
    --peach-light: #fbe9d6;
    --peach: #f2c999;
    --amber: #e6a45c;
    --wine: #8a1c2b;
    --ink: #4a3a30;
    --price: #7b1424;
    --plate-a: #f6efe3;
    --plate-b: #e3c98f;
    --dish-a: #f4ecd2;
    --dish-b: #8aa05a;
  }
  * { box-sizing: border-box; margin: 0; padding: 0; }
  html, body { width: 667px; height: 1200px; overflow: hidden; }
  body {
    position: relative;
    font-family: "Fira Sans Extra Condensed", sans-serif;
    color: var(--ink);
    background:
      linear-gradient(115deg, transparent 30%, rgba(255,255,255,0.75) 44%, rgba(255,255,255,0.2) 56%, transparent 64%),
      radial-gradient(ellipse 70% 40% at 30% 5%, rgba(255,255,255,0.9), transparent 70%),
      linear-gradient(100deg, var(--amber) 0%, var(--peach) 18%, var(--peach-light) 45%, var(--peach) 80%, var(--amber) 100%);
  }
  .page-title {
    position: absolute; top: 40px; left: 0; width: 100%;
    text-align: center;
    font-family: "Josefin Sans", sans-serif;
    font-weight: 100; font-size: 64px; letter-spacing: 6px;
    color: var(--wine);
  }
  .food-photo { position: absolute; }
  .food-photo--fettuccine {
    left: 72px; top: 198px; width: 328px; height: 230px;
    border-radius: 50%;
    background: radial-gradient(ellipse at 55% 45%, var(--plate-b) 0%, var(--plate-a) 45%, #ffffff 70%, #e9e2d8 100%);
    box-shadow: 0 6px 14px rgba(120,70,20,0.25);
  }
  .food-photo--baked {
    left: 68px; top: 822px; width: 332px; height: 206px;
    border-radius: 45% 45% 48% 48% / 40% 40% 60% 60%;
    background: radial-gradient(ellipse at 50% 35%, var(--dish-a) 0%, var(--dish-b) 45%, #f5f1ea 70%, #ddd6cc 100%);
    box-shadow: 0 8px 14px rgba(120,70,20,0.25);
  }
  .menu-item { position: absolute; }
  .menu-item h2 {
    font-weight: 600; font-size: 16px; line-height: 20px;
    color: var(--wine); text-transform: uppercase; margin-bottom: 4px;
  }
  .menu-item--alt h2, .menu-item--alt .row span:first-child { font-style: italic; }
  .row {
    display: flex; justify-content: space-between; align-items: flex-start;
    font-weight: 300; font-size: 10px; line-height: 12.4px;
  }
  .row > span:first-child { white-space: nowrap; }
  .price {
    flex: none;
    font-style: italic; font-weight: 800; font-size: 13px; line-height: 12.4px;
    color: var(--price); width: 18px; text-align: right;
  }
  .row--end { align-items: flex-end; }
  .right { left: 422px; width: 168px; }
  .left { left: 85px; width: 167px; }
  .brand {
    position: absolute; top: 1148px; left: 0; width: 100%;
    text-align: center;
    font-weight: 600; font-size: 16px; letter-spacing: 1px;
    color: var(--wine); text-transform: uppercase;
  }
</style>
</head>
<body>
  <h1 class="page-title">PASTA</h1>

  <div class="food-photo food-photo--fettuccine" role="img" aria-label="Plate of fettuccine alfredo with parsley and a slice of garlic bread"></div>
  <div class="food-photo food-photo--baked" role="img" aria-label="Baked penne with broccoli, mushrooms and melted mozzarella in a white dish with garlic bread"></div>

  <section class="menu-item right" style="top:206px">
    <h2>Penne Ala Rosa</h2>
    <div class="row"><span>Penne with tomato &amp; cream sauce &amp; fresh basil</span><span class="price">29</span></div>
    <div class="row"><span>with chicken,</span><span class="price">39</span></div>
    <div class="row"><span>with shrimp</span><span class="price">44</span></div>
  </section>
  <section class="menu-item right menu-item--alt" style="top:287px">
    <h2>Penne Ala Rosa</h2>
    <div class="row"><span>Penne with tomato &amp; cream sauce &amp; fresh basil</span><span class="price">29</span></div>
    <div class="row"><span>with chicken,</span><span class="price">39</span></div>
    <div class="row"><span>with shrimp</span><span class="price">44</span></div>
  </section>

  <section class="menu-item right" style="top:401px">
    <h2>Spaghetti Bolognese</h2>
    <div class="row"><span>Spaghetti with beef bolognese sauce</span><span class="price">33</span></div>
  </section>
  <section class="menu-item right menu-item--alt" style="top:454px">
    <h2>Spaghetti Bolognese</h2>
    <div class="row"><span>Spaghetti with beef bolognese sauce</span><span class="price">33</span></div>
  </section>

  <section class="menu-item right" style="top:557px">
    <h2>Penne Arrabbiata</h2>
    <div class="row"><span>Penne with spicy tomato sauce &amp; fresh basil</span><span class="price">27</span></div>
    <div class="row"><span>with chicken</span><span class="price">37</span></div>
    <div class="row"><span>with shrimp</span><span class="price">42</span></div>
  </section>
  <section class="menu-item right menu-item--alt" style="top:636px">
    <h2>Penne Arrabbiata</h2>
    <div class="row"><span>Penne with spicy tomato sauce &amp; fresh basil</span><span class="price">27</span></div>
    <div class="row"><span>with chicken</span><span class="price">37</span></div>
    <div class="row"><span>with shrimp</span><span class="price">42</span></div>
  </section>

  <section class="menu-item right" style="top:760px">
    <h2>Fettuccine Alfredo</h2>
    <div class="row"><span>Fettuccine</span></div>
    <div class="row"><span>with creamy white sauce &amp; parmesan cheese</span><span class="price">27</span></div>
    <div class="row"><span>with chicken</span><span class="price">37</span></div>
    <div class="row"><span>with shrimp</span><span class="price">42</span></div>
  </section>
  <section class="menu-item right menu-item--alt" style="top:840px">
    <h2>Fettuccine Alfredo</h2>
    <div class="row"><span>Fettuccine</span></div>
    <div class="row"><span>with creamy white sauce &amp; parmesan cheese</span><span class="price">27</span></div>
    <div class="row"><span>with chicken</span><span class="price">37</span></div>
    <div class="row"><span>with shrimp</span><span class="price">42</span></div>
  </section>

  <section class="menu-item right" style="top:974px">
    <h2>Baked Penne</h2>
    <div class="row"><span>Penne pasta, creamy spinach &amp;<br>mushroom sauce, brocoli, chicken,<br>topped with mozzarella cheese</span><span class="price">39</span></div>
    <div class="row"><span>with Shrimp</span><span class="price">49</span></div>
  </section>
  <section class="menu-item right" style="top:1056px">
    <h2 style="font-style:italic">Baked Penne</h2>
    <div class="row"><span>Penne pasta, creamy spinach &amp;<br>mushroom sauce, brocoli, chicken,<br>topped with mozzarella cheese</span><span class="price">39</span></div>
    <div class="row"><span>with Shrimp</span><span class="price">49</span></div>
  </section>

  <section class="menu-item left" style="top:452px">
    <h2>Lasagna</h2>
    <div class="row"><span>Layers of pasta,<br>&nbsp;beef bolognese, bechamel sauce, t<br>&nbsp;opped with melted mozzarella</span><span class="price">35</span></div>
  </section>
  <section class="menu-item left menu-item--alt" style="top:537px">
    <h2>Lasagna</h2>
    <div class="row"><span>Layers of pasta,<br>beef bolognese, bechamel sauce, t<br>opped with melted mozzarella</span><span class="price">35</span></div>
  </section>

  <section class="menu-item left" style="top:659px">
    <h2>Spaghetti Meatballs</h2>
    <div class="row"><span>Italian style meatballs served<br>with marinara sauce and spaghetti pasta</span><span class="price">37</span></div>
  </section>
  <section class="menu-item left menu-item--alt" style="top:724px">
    <h2>Spaghetti Meatballs</h2>
    <div class="row"><span>Italian style meatballs served<br>with marinara sauce and spaghetti pasta</span><span class="price">37</span></div>
  </section>

  <div class="brand">Amber Fern</div>
</body>
</html>
```